New design for Gift Ledger Website - landing page plus 3 carousel pages

We have a new website we want to launch for 501c3 organizations - Faith-based organizations, not for profit organizations, colleges and universities. Note - this is a design only project. We want to see designs for the landing page and the 3 other pages - Faith-based organizations, not for profit organizations, colleges and universities.
Format: We expect to create this website in Wix so requirement is to make the graphics Wix compatible
See Dossier attached for more details, 4 wireframes (1 landing page and 3 carousel pages), and brand guidelines
Please be creative and and make the visuals engaging. We do NOT want you to simply replicate what is in the wireframe. We are looking for a totally new, fresh and engaging design.
Look and feel
Each slider illustrates characteristics of the customer's brand and the style your logo design should communicate.

```html
<!DOCTYPE html>
<html lang="en">
<head>
<meta charset="utf-8">
<title>Gift Ledger Technologies — 501c3 Organizations</title>
<link href="https://fonts.googleapis.com/css2?family=Montserrat:wght@400;500;600;700;800&display=swap" rel="stylesheet">
<style>
:root{
  --navy:#0c1a3c;
  --navy-deep:#0a1533;
  --green:#1ec98c;
  --green-dark:#12b57b;
  --ink:#111418;
  --grey:#5a6170;
  --line:#d9dce2;
  --soft:#eceef2;
  --white:#ffffff;
}
*{box-sizing:border-box;margin:0;padding:0}
html,body{width:1200px;height:4219px;overflow:hidden}
body{font-family:"Montserrat",Arial,sans-serif;color:var(--ink);background:var(--white);position:relative}
section,header,footer{position:absolute;left:0;width:1200px}
.abs{position:absolute}

/* brand */
.brand{display:flex;align-items:center;gap:12px;font-weight:600;line-height:1.05}
.brand-dot{width:46px;height:46px;border-radius:50%;border:4px solid var(--green)}
.brand-name{font-size:26px}
.brand-name small{display:block;font-size:22px;font-weight:600}

/* hero */
.hero{top:0;height:676px;background:var(--navy)}
.hero .brand{left:85px;top:22px;color:var(--white)}
.nav{left:440px;top:49px;display:flex;gap:32px;font-size:12.5px;font-weight:600;color:var(--white);letter-spacing:.2px}
.login{left:992px;top:33px;width:121px;height:50px;border:1.5px solid #8f9ab3;border-radius:25px;color:var(--white);font-size:12.5px;font-weight:600;display:flex;align-items:center;justify-content:center}
.hero-title{left:85px;top:188px;color:var(--white);font-size:58px;font-weight:800;line-height:68px;letter-spacing:.5px}
.hero-copy{left:85px;top:342px;width:460px;color:#e6e9f0;font-size:14px;line-height:23px}
.segment{top:437px;width:180px;color:var(--green);font-size:17.5px;font-weight:600;line-height:26px}
.segment svg{display:block;margin-bottom:14px}
.hero-art{left:598px;top:160px;width:602px;height:440px;border-radius:200px 0 0 120px;background:radial-gradient(circle at 45% 55%,#5b9cc9 0,#3b6f9e 35%,#e88a6b 60%,#0c1a3c 82%)}

/* process */
.process{top:676px;height:855px;background:linear-gradient(180deg,#fff 0,#fff 36%,#dde0e5 58%,#c9ccd3 100%)}
.process-wave{left:0;top:560px;width:1200px;height:295px;background:linear-gradient(170deg,rgba(255,255,255,0) 20%,rgba(152,226,214,.45) 55%,rgba(255,255,255,.15) 90%)}
.diagram-label{font-size:24px;font-weight:500;text-align:center;line-height:38px;color:var(--ink)}
.process-title{left:700px;width:326px;top:776px;font-size:41px;font-weight:800;text-align:center;letter-spacing:.5px}
.step{width:189px}
.step h3{font-size:26px;font-weight:700;line-height:34px;padding-bottom:5px;border-bottom:1.5px solid #333}
.step p{font-size:12.5px;line-height:21px;color:#333;margin-top:10px}
.step.right{text-align:right}
.btn-white{left:503px;top:1365px;width:193px;height:56px;border-radius:28px;background:var(--white);font-size:14px;font-weight:600;display:flex;align-items:center;justify-content:center}

/* donation */
.donation{top:1531px;height:925px}
.center{left:0;width:1200px;text-align:center}
.h2{font-size:43px;font-weight:800;letter-spacing:.5px}
.sub{font-size:15px;font-weight:500;color:#222}
.give{font-size:28px;font-weight:700;color:var(--green)}
.amounts{left:85px;top:265px;display:flex;gap:25px}
.amount{width:151px;height:54px;border:1.5px solid var(--green);border-radius:27px;color:var(--green);font-size:21px;font-weight:700;display:flex;align-items:center;justify-content:center}
.amount.other{font-size:16px;font-weight:600}
.pay{left:0;width:1200px;top:352px;display:flex;justify-content:center;gap:34px;font-size:19px;font-weight:700;color:var(--navy)}
.pay span{height:54px;display:flex;align-items:center}
.btn-green{left:468px;top:443px;width:264px;height:54px;border-radius:27px;background:var(--green);color:var(--white);font-size:14px;font-weight:600;display:flex;align-items:center;justify-content:center}
.card{top:553px;width:457px;height:260px;background:var(--white);border-radius:14px;box-shadow:0 4px 22px rgba(0,0,0,.12)}
.card svg{position:absolute;left:47px;top:39px}
.card h4{position:absolute;left:175px;top:44px;font-size:21px;font-weight:600;line-height:30px}
.card .brand{position:absolute;left:175px;gap:8px}
.card .brand-dot{width:30px;height:30px;border-width:3px}
.card .brand-name{font-size:15px;color:var(--navy)}
.card .brand-name small{font-size:13px}
.btn-outline{position:absolute;left:175px;top:173px;width:123px;height:50px;border:1.5px solid var(--green);border-radius:25px;color:var(--green);font-size:13px;font-weight:600;display:flex;align-items:center;justify-content:center}

/* video */
.video{top:2456px;height:519px;background:linear-gradient(180deg,#3c4a5b 0,#1d2836 55%,#121a24 100%)}
.video-glow{left:330px;top:160px;width:540px;height:190px;border-radius:20px;background:linear-gradient(180deg,#2f6a45,#1d4a31)}
.play{left:531px;top:189px;width:138px;height:138px;border-radius:50%;background:var(--white);border:8px solid rgba(255,255,255,.55);background-clip:padding-box;display:flex;align-items:center;justify-content:center}

/* enroll */
.enroll{top:2975px;height:410px;border-bottom:1.5px solid var(--line)}
.feature{top:225px;width:320px;display:flex;gap:16px}
.feature h5{font-size:26px;font-weight:700;line-height:30px}
.feature p{font-size:12.5px;line-height:21px;color:#333;margin-top:6px;width:230px}

/* newsletter */
.news{top:3385px;height:544px;overflow:hidden}
.news-lines{left:0;top:300px;width:1200px;height:244px;background:linear-gradient(175deg,rgba(255,255,255,0) 25%,#d8dbe0 60%,rgba(255,255,255,0) 95%)}
.email{left:252px;top:220px;width:519px;height:59px;border-radius:30px;background:var(--soft);color:#9a9fa8;font-size:14px;padding-left:33px;display:flex;align-items:center}
.send{left:789px;top:220px;width:138px;height:59px;border-radius:30px;background:var(--navy);color:var(--white);font-size:15px;font-weight:600;display:flex;align-items:center;justify-content:center}
.agree{left:0;width:1200px;top:292px;display:flex;justify-content:center;align-items:center;gap:12px;font-size:15px;font-weight:500}
.box{width:20px;height:20px;border:1.5px solid #333;border-radius:3px;display:flex;align-items:center;justify-content:center}
.notice{left:295px;width:610px;top:330px;text-align:center;font-size:12.5px;line-height:17px;color:#333}

/* footer */
.footer{top:3929px;height:290px}
.footer .brand{left:470px;top:62px;color:var(--navy)}
.footer .brand-dot{width:58px;height:58px;border-width:5px}
.footer .brand-name{font-size:29px}
.footer .brand-name small{font-size:24px}
.rule{left:85px;width:1030px;height:1.5px;background:#999}
.foot-nav{left:0;width:1200px;top:172px;display:flex;justify-content:center;gap:34px;font-size:13px;font-weight:600}
.copy{top:229px;font-size:12.5px;font-weight:600}
</style>
</head>
<body>

<header class="hero">
  <div class="brand abs"><span class="brand-dot"></span><span class="brand-name">Gift Ledger<small>Technologies</small></span></div>
  <nav class="nav abs"><span>ABOUT US ⌄</span><span>NEWSROOM</span><span>PATENTS</span><span>CLIENTS</span><span>FAQ</span><span>CONTACT</span></nav>
  <div class="login abs">LOG IN</div>
  <h1 class="hero-title abs">501c3<br>ORGANIZATIONS</h1>
  <p class="hero-copy abs">Lorem ipsum dolor sit amet, consectetur adipiscing elit. Maecenas quam risus, semper non nunc nec, egestas tincidunt quam. Duis eu nibh sit amet</p>
  <div class="segment abs" style="left:85px">
    <svg width="68" height="74" viewBox="0 0 68 74"><polygon points="34,2 66,20 66,54 34,72 2,54 2,20" fill="var(--green)"/><circle cx="34" cy="37" r="13" fill="none" stroke="#fff" stroke-width="3"/></svg>
    NON PROFIT<br>ORGANISATION</div>
  <div class="segment abs" style="left:260px">
    <svg width="68" height="74" viewBox="0 0 68 74"><polygon points="34,2 66,20 66,54 34,72 2,54 2,20" fill="var(--green)"/><circle cx="34" cy="37" r="14" fill="#fff"/><circle cx="34" cy="37" r="7" fill="var(--green)"/></svg>
    FAITH-BASED<br>ORGANIZATIONS</div>
  <div class="segment abs" style="left:437px">
    <svg width="68" height="74" viewBox="0 0 68 74"><polygon points="34,2 66,20 66,54 34,72 2,54 2,20" fill="var(--green)"/><rect x="20" y="26" width="28" height="22" rx="3" fill="#fff"/></svg>
    COLLEGES<br>AND UNIVERSITIES</div>
  <div class="hero-art abs" role="img" aria-label="Illustration of donors giving coins and a card through smartphone screens"></div>
</header>

<section class="process">
  <div class="process-wave abs" role="img" aria-label="Decorative dotted wave pattern"></div>
  <div class="diagram-label abs" style="left:187px;width:300px;top:124px">501c3<br>ORGANIZATIONS</div>
  <svg class="abs" style="left:0;top:0" width="600" height="560" viewBox="0 0 600 560">
    <g fill="none" stroke="#333" stroke-width="1.3">
      <line x1="337" y1="377" x2="337" y2="222"/><polyline points="330,234 337,222 344,234"/>
      <line x1="337" y1="377" x2="205" y2="519"/><polyline points="203,505 205,519 217,515"/>
      <line x1="337" y1="377" x2="470" y2="519"/><polyline points="458,515 470,519 468,505"/>
    </g>
  </svg>
  <div class="diagram-label abs" style="left:27px;width:300px;top:544px">DATA OBJECT<br>"DONOR"</div>
  <div class="diagram-label abs" style="left:321px;width:300px;top:544px">DATA EXCHANGE<br>"BUYER"</div>
  <h2 class="process-title abs" style="top:100px">PROCESS</h2>
  <div class="abs" style="left:862px;top:172px;width:1.5px;height:465px;background:#333"></div>
  <div class="step abs" style="left:674px;top:202px"><h3>Step 1</h3><p>Lorem ipsum dolor sit<br>amet, consectetur<br>adipiscing elit.</p></div>
  <div class="step right abs" style="left:864px;top:294px"><h3>Step 2</h3><p>Lorem ipsum dolor sit<br>amet, consectetur<br>adipiscing elit.</p></div>
  <div class="step abs" style="left:674px;top:402px"><h3>Step 3</h3><p>Lorem ipsum dolor sit<br>amet, consectetur<br>adipiscing elit.</p></div>
  <div class="step right abs" style="left:864px;top:487px"><h3>Step 4</h3><p>Lorem ipsum dolor sit<br>amet, consectetur<br>adipiscing elit.</p></div>
  <div class="btn-white abs" style="top:689px">DONATE DATA</div>
</section>

<section class="donation">
  <h2 class="h2 center abs" style="top:98px">MY DONATION</h2>
  <p class="sub center abs" style="top:155px">All donations are tax deductible</p>
  <p class="give center abs" style="top:208px">I want to give</p>
  <div class="amounts abs">
    <span class="amount">$25</span><span class="amount">$50</span><span class="amount">$100</span><span class="amount">$125</span><span class="amount">$150</span><span class="amount other">Other Amount</span>
  </div>
  <div class="pay abs"><span>Veltra</span><span>Cardwell</span><span>Roamly</span><span>Atlas Pay</span><span>PayNest</span></div>
  <div class="btn-green abs">DONATE WITH CREDIT CARD</div>
  <div class="card abs" style="left:121px">
    <svg width="96" height="108" viewBox="0 0 96 108"><polygon points="48,2 94,28 94,80 48,106 2,80 2,28" fill="var(--green)"/><circle cx="48" cy="54" r="17" fill="none" stroke="#fff" stroke-width="3"/></svg>
    <h4>Donate with Crypto<br>Powered by GLT</h4>
    <div class="brand" style="top:108px"><span class="brand-dot"></span><span class="brand-name">Gift Ledger<small>Technologies</small></span></div>
    <span class="btn-outline">DONATE</span>
  </div>
  <div class="card abs" style="left:617px">
    <svg width="96" height="108" viewBox="0 0 96 108"><polygon points="48,2 94,28 94,80 48,106 2,80 2,28" fill="var(--green)"/><ellipse cx="48" cy="42" rx="16" ry="6" fill="none" stroke="#fff" stroke-width="3"/><path d="M32 42v24c0 3 7 6 16 6s16-3 16-6V42" fill="none" stroke="#fff" stroke-width="3"/></svg>
    <h4>Donate with Data</h4>
    <div class="brand" style="top:80px"><span class="brand-dot"></span><span class="brand-name">Gift Ledger<small>Technologies</small></span></div>
    <span class="btn-outline">DONATE</span>
  </div>
</section>

<section class="video" role="img" aria-label="Photo of a finger pressing a green Donate key on a keyboard">
  <div class="video-glow abs"></div>
  <div class="play abs"><svg width="46" height="50" viewBox="0 0 46 50"><polygon points="4,2 44,25 4,48" fill="var(--green)"/></svg></div>
</section>

<section class="enroll">
  <h2 class="h2 center abs" style="top:100px">WHY ENROLL!</h2>
  <p class="sub center abs" style="top:158px">To get full access to all the features, start by creating an account</p>
  <div class="feature abs" style="left:85px">
    <svg width="70" height="70" viewBox="0 0 70 70" fill="none" stroke="var(--green-dark)" stroke-width="4"><rect x="4" y="10" width="62" height="56" rx="6" stroke="var(--navy)"/><line x1="4" y1="24" x2="66" y2="24"/><line x1="18" y1="4" x2="18" y2="16"/><line x1="52" y1="4" x2="52" y2="16"/><g stroke="var(--navy)" stroke-width="5"><line x1="15" y1="36" x2="20" y2="36"/><line x1="28" y1="36" x2="33" y2="36"/><line x1="41" y1="36" x2="46" y2="36"/><line x1="54" y1="36" x2="58" y2="36"/><line x1="15" y1="50" x2="20" y2="50"/><line x1="28" y1="50" x2="33" y2="50"/><line x1="41" y1="50" x2="46" y2="50"/></g></svg>
    <div><h5>Drops</h5><p>Purchase NFTs that are directly sold by top Creators</p></div>
  </div>
  <div class="feature abs" style="left:437px">
    <svg width="70" height="70" viewBox="0 0 70 70" fill="none" stroke="var(--navy)" stroke-width="4"><path d="M8 6h54l6 18H2z" stroke="var(--green-dark)"/><path d="M2 24c0 6 11 6 11 0 0 6 11 6 11 0 0 6 11 6 11 0 0 6 11 6 11 0 0 6 11 6 11 0 0 6 11 6 11 0" stroke="var(--green-dark)"/><path d="M8 34v32h54V34"/><rect x="26" y="44" width="18" height="22"/></svg>
    <div><h5>Marketplace</h5><p>Bid on and auction off rare digital collectibles</p></div>
  </div>
  <div class="feature abs" style="left:789px">
    <svg width="64" height="70" viewBox="0 0 64 70"><polygon points="32,3 61,19 61,51 32,67 3,51 3,19" fill="none" stroke="var(--navy)" stroke-width="4"/><text x="32" y="41" text-anchor="middle" font-family="Montserrat,sans-serif" font-weight="800" font-size="17" fill="var(--green-dark)">NFT</text></svg>
    <div><h5>My NFTs</h5><p>A digital gallery to showcase your collection</p></div>
  </div>
</section>

<section class="news">
  <div class="news-lines abs" role="img" aria-label="Decorative flowing line pattern"></div>
  <h2 class="h2 center abs" style="top:103px;color:var(--navy)">NEVER MISS A DROP</h2>
  <p class="sub center abs" style="top:162px">Subscribe for the latest news, drops &amp; collectibles</p>
  <div class="email abs">Email</div>
  <div class="send abs">SEND</div>
  <div class="agree abs"><span class="box"><svg width="14" height="12" viewBox="0 0 14 12"><polyline points="1,6 5,10 13,1" fill="none" stroke="#333" stroke-width="2"/></svg></span>By entering my email and subscribing I confirm and agree to the above.</div>
  <p class="notice abs">After rending the Privacy Notice, you may subscribe for our newsletter to get special offers and occasional surveys delivered to your inbox. Unsubscribe at any time by clicking on the link in the email.</p>
</section>

<footer class="footer">
  <div class="brand abs"><span class="brand-dot"></span><span class="brand-name">Gift Ledger<small>Technologies</small></span></div>
  <div class="rule abs" style="top:154px"></div>
  <nav class="foot-nav abs"><span>ABOUT US</span><span>NEWSROOM</span><span>PATENTS</span><span>CLIENTS</span><span>FAQ</span><span>CONTACT</span></nav>
  <div class="rule abs" style="top:208px"></div>
  <p class="copy center abs">Copyright 2022.All right reserved</p>
</footer>

</body>
</html>
```